Marketing One-Sheet for Security Deposit Claim Notice

I need a one-sheet flyer formatted for email distribution — optimized as a JPEG/PNG that I can insert into Constant Contact or Outlook. I do not want to attach it to an email, but insert it in the email we send out. I would like it to look professional but engaging. Some images would be good, but want to make sure it reads well if images do not load for the recipients. The text is in the attached Word document, but I am open to changes/ideas that may be better for marketing purposes. I included the URLs for some of the links I would like in the one-sheet that is clickable. The logo for the business is being uploaded on the Word document. Proposed text is also uploaded in a Word document. Thank you.

Target Market(s)

Landlords, Real Estate Agents, Property Managers

Industry/Entity Type

Legal

Requirements
Must have
• Professional but appealing design. The One-sheet is going to be placed in the body of emails, not as an attachment.
Nice to have
• Include our logo for the business and the web links please.
Should not have
• Images can be ok, but it needs to look right if images do not download from the email sent out.

```html
<!DOCTYPE html>
<html lang="en">
<head>
<meta charset="utf-8">
<title>Security Deposit Claim Notice – Keystone Landlord Law</title>
<link href="https://fonts.googleapis.com/css2?family=Cinzel:wght@700;800&family=Red+Hat+Display:wght@400;500;700;800&display=swap" rel="stylesheet">
<style>
  :root{
    --red:#b8202f;
    --cream:#f8efc4;
    --cream-bg:#f7f3d6;
    --ink:#1b1b1b;
    --body:#2a2a2a;
    --muted:#555555;
    --black:#050505;
    --white:#ffffff;
    --line:#e2e2e2;
    --page:#eeeeee;
  }
  *{box-sizing:border-box;margin:0;padding:0}
  html,body{width:1200px;height:1117px;overflow:hidden;background:var(--page)}
  .flyer{
    position:absolute;left:219px;top:20px;width:762px;height:1077px;
    background:var(--white);overflow:hidden;
    font-family:"Red Hat Display",sans-serif;color:var(--ink);
    box-shadow:0 2px 10px rgba(0,0,0,.12);
  }
  .hero-photo{
    position:absolute;top:0;left:292px;width:470px;height:209px;
    background:linear-gradient(110deg,#3a4250 0%,#6b7380 35%,#c9c2b4 65%,#8d8a86 100%);
    clip-path:polygon(0 0,100% 0,100% 100%,54px 100%);
  }
  .brand{position:absolute;left:68px;top:44px;width:230px}
  .brand-name{
    display:flex;align-items:center;gap:10px;
    font-weight:700;font-size:28px;line-height:31px;color:var(--red);
  }
  .brand-mark{width:16px;height:16px;background:var(--red);flex:none}
  .brand-tagline{margin-top:10px;font-size:10.5px;line-height:13px;font-weight:500;color:var(--muted);width:170px}
  .brand-contact{margin-top:6px;font-weight:700;font-size:15px;line-height:19px;color:var(--red)}
  .headline-band{
    position:absolute;top:209px;left:0;width:762px;height:123px;background:var(--red);
    display:flex;align-items:center;justify-content:center;text-align:center;
  }
  .headline{font-family:"Cinzel",serif;font-weight:800;font-size:46px;line-height:46px;color:var(--cream)}
  .requirements-title{
    position:absolute;top:352px;left:0;width:762px;text-align:center;
    font-family:"Cinzel",serif;font-weight:700;font-size:22px;color:var(--red);
  }
  .requirements{
    position:absolute;top:392px;left:53px;width:658px;height:91px;
    background:var(--black);border-radius:16px;display:flex;align-items:center;
  }
  .requirement{flex:1;display:flex;align-items:center;gap:12px;padding-left:24px;height:64px}
  .requirement + .requirement{border-left:2px solid var(--white)}
  .requirement-icon{width:61px;height:61px;flex:none}
  .requirement-text{color:var(--white);font-weight:700;font-size:15.5px;line-height:16.5px}
  .warning{
    position:absolute;top:512px;left:53px;width:308px;height:239px;
    background:var(--red);border-radius:16px;padding:16px 14px 0 24px;color:var(--white);
  }
  .warning-title{font-family:"Cinzel",serif;font-weight:700;font-size:26px;line-height:25px;margin-bottom:16px;white-space:nowrap}
  .warning-list{list-style:none}
  .warning-list li{position:relative;padding-left:20px;font-size:17px;line-height:19px;margin-bottom:14px}
  .warning-list li strong{font-weight:800;display:block}
  .warning-list svg{position:absolute;left:0;top:3px;width:13px;height:13px}
  .explainer{
    position:absolute;top:532px;left:391px;width:310px;white-space:nowrap;
    font-size:15px;line-height:18.4px;letter-spacing:.15px;color:var(--body);
  }
  .explainer strong{font-weight:800;color:var(--black)}
  .price{
    position:absolute;left:53px;width:658px;border:2px solid var(--line);border-radius:8px;
    display:flex;align-items:center;justify-content:center;text-align:center;
    font-weight:700;font-size:22px;line-height:25px;background:var(--white);
  }
  .price-amount{color:var(--red)}
  .price--residential{top:770px;height:72px}
  .price--commercial{top:852px;height:43px}
  .footer-band{position:absolute;left:0;top:969px;width:762px;height:108px;background:var(--cream-bg)}
  .cta{
    position:absolute;top:927px;left:99px;width:564px;height:50px;
    border:2px solid var(--red);border-radius:25px;background:var(--white);
    display:flex;align-items:center;overflow:hidden;text-decoration:none;
  }
  .cta-label{flex:1;padding-left:20px;font-weight:700;font-size:25px;color:var(--black)}
  .cta-button{
    height:100%;width:263px;background:var(--red);border-radius:25px;
    color:var(--white);font-weight:800;font-size:37px;display:flex;align-items:center;justify-content:center;
  }
  .cta-cursor{position:absolute;top:967px;left:630px;width:46px;height:46px}
  .contact-line{
    position:absolute;top:1013px;left:0;width:762px;text-align:center;
    font-weight:700;font-size:19px;color:var(--black);
  }
</style>
</head>
<body>
<main class="flyer">
  <div class="hero-photo" role="img" aria-label="Photo of a businessman slipping cash into his jacket while a tenant signs paperwork at a desk"></div>

  <div class="brand">
    <div class="brand-name"><span>Keystone<br>Landlord Law</span><span class="brand-mark"></span></div>
    <p class="brand-tagline">Legal help for property owners, investors and managers</p>
    <p class="brand-contact">KeystoneLandlordLaw.com<br>1(800) 555-0142</p>
  </div>

  <header class="headline-band">
    <h1 class="headline">Landlord, need to keep<br>the Security Deposit?</h1>
  </header>

  <h2 class="requirements-title">Security Deposit Claim Notice requirements:</h2>

  <section class="requirements">
    <div class="requirement">
      <svg class="requirement-icon" viewBox="0 0 61 61">
        <circle cx="30.5" cy="30.5" r="29" fill="#b8202f" stroke="#fff" stroke-width="3"/>
        <circle cx="29" cy="30" r="14" fill="none" stroke="#fff" stroke-width="2.5"/>
        <path d="M29 21v9h-6" fill="none" stroke="#fff" stroke-width="2.5" stroke-linecap="round"/>
        <circle cx="39" cy="39" r="7" fill="#fff"/>
        <path d="M35.5 39l2.5 2.5 4.5-5" fill="none" stroke="#b8202f" stroke-width="2"/>
      </svg>
      <p class="requirement-text">Must be<br>served on time</p>
    </div>
    <div class="requirement">
      <svg class="requirement-icon" viewBox="0 0 61 61">
        <circle cx="30.5" cy="30.5" r="29" fill="#b8202f" stroke="#fff" stroke-width="3"/>
        <g fill="none" stroke="#fff" stroke-width="2.2" stroke-linecap="round">
          <path d="M30.5 17v24M18 22h25M22 42h17"/>
          <path d="M19 23l-5 10h10zM42 23l-5 10h10z"/>
          <path d="M14 33a5 4 0 0 0 10 0M37 33a5 4 0 0 0 10 0"/>
        </g>
      </svg>
      <p class="requirement-text">Must be served<br>according to<br>Florida law</p>
    </div>
    <div class="requirement">
      <svg class="requirement-icon" viewBox="0 0 61 61">
        <circle cx="30.5" cy="30.5" r="29" fill="#b8202f" stroke="#fff" stroke-width="3"/>
        <text x="30.5" y="39" text-anchor="middle" fill="#fff" font-family="Red Hat Display, sans-serif" font-weight="700" font-size="24">Aa</text>
      </svg>
      <p class="requirement-text">Must contain<br>specific wording</p>
    </div>
  </section>

  <section class="warning">
    <h3 class="warning-title">Security Deposit<br>Claim Notice<br>not correct, then</h3>
    <ul class="warning-list">
      <li><svg viewBox="0 0 13 13"><circle cx="6.5" cy="6.5" r="6.5" fill="#fff"/><path d="M3.5 6.7l2 2 4-4" fill="none" stroke="#b8202f" stroke-width="1.8"/></svg>tenant could demand return of <strong>FULL SECURITY DEPOSIT</strong></li>
      <li><svg viewBox="0 0 13 13"><circle cx="6.5" cy="6.5" r="6.5" fill="#fff"/><path d="M3.5 6.7l2 2 4-4" fill="none" stroke="#b8202f" stroke-width="1.8"/></svg>tenant can sue and recover <strong>LEGAL FEES FROM THE LANDLORD</strong></li>
    </ul>
  </section>

  <p class="explainer">There are lawyers that specialize in<br>representing <strong>TENANTS</strong> against landlords for<br>not making a proper claim on the security<br>deposit. They can win the case and recover<br>thousands of dollars <strong>$$</strong> in legal fees from the<br>Landlord. Plus, the tenant can get back 100%<br>of the Security Deposit, even if they owe<br>the Landlord unpaid rent or caused damages<br>to the property. Florida law helps the tenants<br>if the Security Deposit Claim Notice is not<br>served on time and correctly.</p>

  <p class="price price--residential"><span><span class="price-amount">$350</span> Flat Fee to prepare and serve Security Deposit Claim<br>Notices for Landlords.</span></p>
  <p class="price price--commercial"><span><span class="price-amount">$450</span> for commercial properties</span></p>

  <div class="footer-band"></div>

  <a class="cta" href="#">
    <span class="cta-label">Want more information</span>
    <span class="cta-button">CLICK HERE</span>
  </a>
  <svg class="cta-cursor" viewBox="0 0 46 46">
    <g stroke="#f2a21b" stroke-width="2.5" stroke-linecap="round">
      <path d="M6 8l4 4M14 3v5M2 16h5M4 25l4-3"/>
    </g>
    <path d="M14 16l28 10-12 3-5 12z" fill="#2d4fbf"/>
  </svg>

  <p class="contact-line">Contact Us to prepare the Security Deposit Claim Notice.</p>
</main>
</body>
</html>
```